Cafe Menu for Willow Lantern Cafe

Menu designed for my cafe. I need multiple sizes to be created.
DL pamphlet
A4
and I also need 5 x A3 portraits & 5 x A3 landscapes. The menu must be spread out over a total of 10 A3 pages. I have uploaded my logo which needs to be used & I would like the colours from the logo used. The background of the menu needs to be white. I have uploaded an image on another menu for which I would like the same heading font to be used.

Target Market(s)

cafe, restaurant

Font styles to use
Serif
Decorative
Script

Requirements
Must have
• White back ground
correct font as I have uploaded
Nice to have
• May have drawings of food in back and white.

```html
<!DOCTYPE html>
<html lang="en">
<head>
<meta charset="utf-8">
<title>Willow Lantern Cafe Menu</title>
<link rel="stylesheet" href="https://fonts.googleapis.com/css2?family=Great+Vibes&family=Kaushan+Script&family=Playfair+Display:ital,wght@1,500;1,600&family=Poppins:wght@400;500&display=swap">
<style>
  :root {
    --backdrop: #fdf3d0;
    --ink: #1f1f1f;
    --yellow: #f9c804;
    --white: #ffffff;
    --olive: #7d8c3c;
    --photo-green-a: #3d4a32;
    --photo-green-b: #8c9a78;
    --photo-dark-a: #2a2522;
    --photo-dark-b: #7a4a2a;
  }
  * { box-sizing: border-box; margin: 0; padding: 0; }
  html, body { width: 1171px; height: 1200px; overflow: hidden; }
  body { background: var(--backdrop); position: relative; font-family: "Poppins", sans-serif; }

  .menu-page {
    position: absolute; top: 49px; width: 506px; height: 1072px;
    background: var(--ink); overflow: hidden;
    box-shadow: 0 12px 18px -10px rgba(0,0,0,.35);
  }
  .menu-page--drinks { left: 51px; }
  .menu-page--food { left: 614px; }

  .column-yellow { position: absolute; top: 0; bottom: 0; right: 0; background: var(--yellow); }
  .menu-page--drinks .column-yellow { left: 244px; }
  .menu-page--food .column-yellow { left: 260px; }

  .hero { position: absolute; left: 0; top: 0; width: 506px; height: 210px; }

  .brand-seal {
    position: absolute; left: 174px; top: 24px; width: 162px; height: 162px;
    border-radius: 50%; background: var(--white); border: 7px solid var(--yellow);
    display: flex; flex-direction: column; align-items: center; justify-content: center;
    text-align: center;
  }
  .brand-name { font-family: "Poppins", sans-serif; font-weight: 500; font-size: 14px; line-height: 1.2; color: var(--olive); width: 110px; margin-top: 6px; }
  .brand-tagline { font-size: 12px; color: var(--ink); margin-top: 8px; }
  .brand-address { font-size: 6.5px; color: var(--ink); margin-top: 14px; }
  .brand-phone { font-size: 9px; color: var(--ink); margin-top: 2px; }

  .section-badge {
    position: absolute; width: 130px; height: 43px;
    border-radius: 22px 12px 26px 10px / 16px 24px 14px 22px;
    display: flex; align-items: center; justify-content: center;
    font-family: "Great Vibes", cursive; font-size: 24px; transform: translateX(-50%) rotate(-1.5deg);
  }
  .section-badge--dark { background: var(--ink); color: var(--white); }
  .section-badge--light { background: var(--yellow); color: var(--ink); }

  .item-list { position: absolute; list-style: none; }
  .item-list--on-yellow { color: var(--ink); }
  .item-list--on-black { color: var(--white); }

  .item-row {
    display: flex; align-items: baseline; height: 20.5px;
    font-family: "Playfair Display", serif; font-style: italic; font-weight: 600;
    font-size: 12.5px; letter-spacing: .6px; white-space: nowrap;
  }
  .item-list--coffee .item-row { height: 21.7px; }
  .item-list--frappes .item-row, .item-list--frappes .item-note { height: 21.6px; }
  .item-leader { flex: 1; border-bottom: 1px dotted currentColor; margin: 0 4px; transform: translateY(-3px); opacity: .8; }
  .item-note { font-size: 8.4px; height: 20.5px; display: flex; align-items: center; white-space: nowrap; }
  .item-note--small { font-size: 6.4px; }
  .item-note--wrap { height: 16px; }

  .dish { margin-bottom: 2.5px; }
  .dish .item-row { height: 18px; }
  .dish--spaced { margin-bottom: 14px; }
  .dish-desc { font-size: 6.5px; line-height: 11.7px; }

  .info-card {
    position: absolute; background: var(--white); border-radius: 8px;
    display: flex; flex-direction: column; align-items: center; justify-content: center;
    font-family: "Kaushan Script", cursive; font-size: 11px; line-height: 19.5px; color: var(--ink);
    text-align: center;
  }
  .info-card--left { left: 13px; top: 535px; width: 216px; height: 130px; border: 4px solid var(--yellow); }
  .info-card--right { left: 271px; top: 914px; width: 223px; height: 134px; border: 2.5px solid var(--ink); }

  .sketch-area { position: absolute; left: 0; top: 215px; width: 244px; height: 857px; background: var(--ink); opacity: 0; }
</style>
</head>
<body>

<section class="menu-page menu-page--drinks" aria-label="Drinks menu">
  <div class="column-yellow"></div>
  <div class="sketch-area" role="img" aria-label="White line drawings of food and drinks"></div>

  <svg class="hero" viewBox="0 0 506 210" role="img" aria-label="Photo of fresh green vegetables and herbs">
    <defs>
      <linearGradient id="greens" x1="0" y1="0" x2="1" y2="1">
        <stop offset="0" stop-color="var(--photo-green-a)"/>
        <stop offset=".5" stop-color="var(--photo-green-b)"/>
        <stop offset="1" stop-color="var(--photo-green-a)"/>
      </linearGradient>
    </defs>
    <path d="M0 0H506V154Q380 200 244 206Q110 205 0 172Z" fill="url(#greens)"/>
  </svg>

  <div class="brand-seal">
    <div class="brand-name">Willow Lantern Cafe</div>
    <div class="brand-tagline">Coffee, breakfast &amp; lunch</div>
    <div class="brand-address">14 Harrow Lane, Ashby Q</div>
    <div class="brand-phone">Phone: 07 4000 1234</div>
  </div>

  <div class="section-badge section-badge--dark" style="left:372px;top:238px">Cold Drinks</div>
  <ul class="item-list item-list--on-yellow" style="left:262px;top:296px;width:227px">
    <li class="item-row">Milkshake<span class="item-leader"></span>$7.00</li>
    <li class="item-row">Thickshake<span class="item-leader"></span>$8.00</li>
    <li class="item-note item-note--small">Flavours - Chocolate, vanilla, strawberry, banana, caramel &amp; coffee</li>
    <li class="item-row">Iced Latte<span class="item-leader"></span>$7.50</li>
    <li class="item-note">Add syrup: vanilla, caramel, white chocolate, hazelnut</li>
    <li class="item-row">Iced Coffee<span class="item-leader"></span>$8.00</li>
    <li class="item-row">Iced Chocolate<span class="item-leader"></span>$8.00</li>
    <li class="item-row">Iced Mocha<span class="item-leader"></span>$8.00</li>
  </ul>

  <div class="section-badge section-badge--dark" style="left:374px;top:489px">Juice Bar</div>
  <ul class="item-list item-list--on-yellow" style="left:263px;top:546px;width:226px">
    <li class="item-row">Passion Pop<span class="item-leader"></span>$9.00</li>
    <li class="item-note">Passionfruit, apple &amp; oranges</li>
    <li class="item-row">Sweet Juice<span class="item-leader"></span>$9.00</li>
    <li class="item-row">Apple, pineapple, oranges &amp; mango</li>
    <li class="item-row">Orange Juice<span class="item-leader"></span>$9.00</li>
    <li class="item-note">Freshly juiced oranges</li>
  </ul>

  <div class="section-badge section-badge--dark" style="left:374px;top:686px">Smoothies</div>
  <ul class="item-list item-list--on-yellow" style="left:264px;top:743px;width:225px">
    <li class="item-row">Mango Raspberry Smoothie<span class="item-leader"></span>$9.00</li>
    <li class="item-note item-note--small">Frozen mango &amp; raspberry sorbet blended with coconut milk</li>
    <li class="item-row">Mango Coconut Smoothie<span class="item-leader"></span>$9.00</li>
    <li class="item-note">Frozen mango blended with coconut milk</li>
    <li class="item-row">Berry Blast Smoothie<span class="item-leader"></span>$9.00</li>
    <li class="item-note">Mixed berries blended with coconut milk</li>
    <li class="item-row">Choc Banana Smoothie<span class="item-leader"></span>$9.00</li>
    <li class="item-note item-note--wrap">Frozen banana &amp; dark chocolate ice cream</li>
    <li class="item-note item-note--wrap">blended together with whole milk</li>
  </ul>

  <div class="info-card info-card--left">
    <p>14 Harrow Lane, Ashby Q 4720</p>
    <p>Phone Orders Welcome! 07 4000 1234</p>
    <p>Open 7 Days From 7am</p>
    <p>Open Weekends</p>
    <p>Saturday &amp; Sunday 7am-12pm</p>
  </div>
</section>

<section class="menu-page menu-page--food" aria-label="Coffee and food menu">
  <div class="column-yellow"></div>

  <svg class="hero" viewBox="0 0 506 210" role="img" aria-label="Photo of colourful dishes on a dark table">
    <defs>
      <linearGradient id="dishes" x1="0" y1="0" x2="1" y2="1">
        <stop offset="0" stop-color="var(--photo-dark-a)"/>
        <stop offset=".5" stop-color="var(--photo-dark-b)"/>
        <stop offset="1" stop-color="var(--photo-dark-a)"/>
      </linearGradient>
    </defs>
    <path d="M0 0H506V185Q390 150 260 147Q120 150 0 185Z" fill="url(#dishes)"/>
  </svg>

  <div class="section-badge section-badge--light" style="left:128px;top:208px">Frappes</div>
  <ul class="item-list item-list--on-black item-list--frappes" style="left:12px;top:268px;width:234px">
    <li class="item-row">Strawberry Lemonade Frappe<span class="item-leader"></span>$9.00</li>
    <li class="item-note">Strawberry syrup blended together with lemonade &amp; ice</li>
    <li class="item-row">Coffee Frappe<span class="item-leader"></span>$9.00</li>
    <li class="item-note">Espresso blended with milk &amp; ice, topped with cream</li>
    <li class="item-row">Chocolate Frappe</li>
    <li class="item-note">Chocolate syrup blended with milk &amp; ice, topped with cream</li>
  </ul>

  <div class="section-badge section-badge--light" style="left:128px;top:420px">Coffee Menu</div>
  <ul class="item-list item-list--on-black item-list--coffee" style="left:12px;top:481px;width:234px">
    <li class="item-row">Cappuccino<span class="item-leader"></span>$4.80</li>
    <li class="item-row">Flat White<span class="item-leader"></span>$4.80</li>
    <li class="item-row">Latte<span class="item-leader"></span>$5.00</li>
    <li class="item-row">Long Black<span class="item-leader"></span>$4.80</li>
    <li class="item-row">Mocha<span class="item-leader"></span>$5.20</li>
    <li class="item-row">Macchiato<span class="item-leader"></span>$3.50</li>
    <li class="item-row">Espresso<span class="item-leader"></span>$3.50</li>
    <li class="item-row">Chai Latte<span class="item-leader"></span>$4.80</li>
    <li class="item-row">Hot Chocolate<span class="item-leader"></span>$4.80</li>
    <li class="item-row">Tea<span class="item-leader"></span>$4.50</li>
    <li class="item-note item-note--small">Tea Flavours: English breakfast, earl grey, green, berry green &amp; coconut</li>
  </ul>

  <div class="section-badge section-badge--light" style="left:128px;top:742px;width:162px">Takeaway Coffee</div>
  <ul class="item-list item-list--on-black" style="left:12px;top:803px;width:234px">
    <li class="item-row" style="height:21.5px">Takeaway Large<span class="item-leader"></span>$6.80</li>
    <li class="item-row" style="height:21.5px">Takeaway Regular<span class="item-leader"></span>$5.20</li>
    <li class="item-row" style="height:21.5px">Takeaway Small<span class="item-leader"></span>$4.80</li>
  </ul>

  <div class="section-badge section-badge--light" style="left:128px;top:887px;width:162px">Coffee Extras</div>
  <ul class="item-list item-list--on-black" style="left:12px;top:947px;width:234px">
    <li class="item-row" style="height:21.5px">Mug &amp; Extra Shot<span class="item-leader"></span>50c</li>
    <li class="item-row" style="height:21.5px">Soy &amp; Lactose Free Milk<span class="item-leader"></span>80c</li>
    <li class="item-row" style="height:21.5px">Syrups<span class="item-leader"></span>$1.00</li>
  </ul>

  <div class="section-badge section-badge--dark" style="left:380px;top:219px">Kids Menu</div>
  <ul class="item-list item-list--on-yellow" style="left:272px;top:275px;width:225px">
    <li class="item-row" style="height:19.6px">Scrambled Eggs<span class="item-leader"></span>$9.50</li>
    <li class="item-note" style="height:19.6px">Two eggs scrambled with toast &amp; tomato sauce</li>
    <li class="item-row" style="height:19.6px">Rainbow Pancakes<span class="item-leader"></span>$9.50</li>
    <li class="item-note item-note--small" style="height:19.6px;font-size:7.4px">Two small pancakes served with ice cream &amp; sprinkles</li>
    <li class="item-row" style="height:19.6px">Nuggets &amp; Chips<span class="item-leader"></span>$8.00</li>
    <li class="item-row" style="height:19.6px">Chicken Chippees<span class="item-leader"></span>$8.50</li>
  </ul>

  <div class="section-badge section-badge--dark" style="left:380px;top:418px;width:152px">Breakfast Menu</div>
  <ul class="item-list item-list--on-yellow" style="left:268px;top:474px;width:229px">
    <li class="dish">
      <div class="item-row">Big Breakfast<span class="item-leader"></span>$21.50</div>
      <p class="dish-desc">Bacon, sausages, hash browns, tomato, baked beans &amp; mushrooms with a slice of toasted panini bread &amp; your choice of fried, poached or scrambled eggs.</p>
    </li>
    <li class="dish">
      <div class="item-row">Classic Breakfast<span class="item-leader"></span>$16.500</div>
      <p class="dish-desc">Your choice of fried poached or scrambled eggs served with either bacon or sausages, tomato &amp; a slice of panini toast</p>
    </li>
    <li class="dish">
      <div class="item-row">Avocado Stack<span class="item-leader"></span>$17.00</div>
      <p class="dish-desc">Turkish bread topped with avocado, bacon or salmon, 2 poached eggs &amp; a sprinkle of feta cheese poached or scrambled eggs.</p>
    </li>
    <li class="dish">
      <div class="item-row">Eggs Benedict<span class="item-leader"></span>$19.00</div>
      <p class="dish-desc">Your choice of bacon, ham or salmon served with toasted turkish bread, poached eggs &amp; creamy hollandaise sauce</p>
    </li>
    <li class="dish">
      <div class="item-row">Classic Omelet<span class="item-leader"></span>$17.50</div>
      <p class="dish-desc">Ham, tomato, spinach, onion &amp; cheese omelet topped with fried cherry tomatoes &amp; turkish toast</p>
    </li>
    <li class="dish">
      <div class="item-row">Panini Scramble<span class="item-leader"></span>$16.50</div>
      <p class="dish-desc">Toasted panini bread topped with scrambled eggs, sautéed mushrooms, cherry tomatoes &amp; spinach with a drizzle of hollandaise sauce on top</p>
    </li>
    <li class="dish dish--spaced">
      <div class="item-row">Breaky Wrap<span class="item-leader"></span>$15.00</div>
      <p class="dish-desc">Bacon, eggs, hash browns, cheese &amp; BBQ sauce on a toasted wrap</p>
    </li>
    <li class="dish">
      <div class="item-row">Ultimate Breakfast Toastie<span class="item-leader"></span>$14.50</div>
      <p class="dish-desc">Bacon, scrambled eggs, smashed avocado, spinach &amp; feta with hollandaise sauce on a toasted ciabatta sandwich roll</p>
    </li>
    <li class="dish">
      <div class="item-row">Breakfast Share Plate<span class="item-leader"></span>$28.50</div>
      <p class="dish-desc">A delicious selection of yummy breakfast items including bacon, scrambled eggs, hash browns, croissant, yogurt, strawberries &amp;</p>
    </li>
  </ul>

  <div class="info-card info-card--right">
    <p>14 Harrow Lane, Ashby Q 4720</p>
    <p>Phone Orders Welcome! 07 4000 1234</p>
    <p>Open 7 Days From 7am</p>
    <p>Open Weekends</p>
    <p>Saturday &amp; Sunday 7am-12pm</p>
  </div>
</section>

</body>
</html>
```